Kelvaro Video on Demand iPad App UI Design

Kelvaro is part of a VOD(Video On Demand) platform, a close match to our requirement is Brimlane.

We are looking for flat ui design endorsed by quorrel is design guidelines. We have been through the exercise of creating mock ups to guide your thoughts. You don't have to copy the exact concept in mock ups, rather present us with a more creative way of laying out stuff as its dictated in mockups

Along with the screen work we would also like ideas on logo design

You don't have to cover design for all 6 screens attached as long as you can do the main page, detail page and and menu system, you can complete the rest once selected.

Project Deadline Extended
Reason: We have not received enough designs in order to make a decision yet.

Target Market(s)

Video on demand

Industry/Entity Type

Work

Font styles to use
Other font styles liked:
• something that appears very fine on retina devices

Requirements
Must have
• Fully built out screens, with psd files or illustrator files
Nice to have
• have a look at ostrevo tv app, brimlane or tandle movies
Should not have
• no gradients, i have has to be a flat solid color design

```html
<!DOCTYPE html>
<html lang="en">
<head>
<meta charset="utf-8">
<title>Kelvaro – Video Detail</title>
<link rel="stylesheet" href="https://fonts.googleapis.com/css2?family=Open+Sans:wght@400;600&family=Arimo:wght@400&display=swap">
<style>
  :root {
    --page-bg: #ffffff;
    --screen-bg: #161616;
    --header-bg: #d9a400;
    --player-bg: #282828;
    --title-band: #525252;
    --body-bg: #0c0c0c;
    --footer-bg: #151515;
    --text-light: #ffffff;
    --text-soft: #eeeeee;
    --rule: #d8d8d8;
  }
  * { margin: 0; padding: 0; box-sizing: border-box; }
  html, body {
    width: 1200px; height: 823px; overflow: hidden;
    background: var(--page-bg);
  }
  .app-screen {
    position: absolute; left: 123px; top: 0;
    width: 839px; height: 724px;
    transform: scale(1.1368); transform-origin: top left;
    background: var(--screen-bg);
    font-family: "Open Sans", sans-serif;
    color: var(--text-light);
  }
  .app-header {
    position: absolute; left: 0; top: 27px; width: 839px; height: 77px;
    background: var(--header-bg);
  }
  .app-name {
    position: absolute; left: 36px; top: 20px;
    font-weight: 400; font-size: 28px; line-height: 36px;
  }
  .header-search { position: absolute; left: 698px; top: 22px; }
  .header-menu { position: absolute; left: 777px; top: 21px; }
  .video-player {
    position: absolute; left: 37px; top: 126px; width: 760px; height: 267px;
    background: var(--player-bg);
  }
  .play-button { position: absolute; left: 385px; top: 110px; }
  .video-actions {
    position: absolute; top: 412px; left: 0; width: 839px; height: 70px;
  }
  .action {
    position: absolute; top: 0; width: 130px; margin-left: -65px;
    text-align: center; font-size: 19.5px; font-weight: 600; line-height: 24px;
    white-space: nowrap;
  }
  .action svg { display: block; margin: 0 auto 6px; height: 34px; }
  .action-watch { left: 265px; }
  .action-like { left: 376px; }
  .action-share { left: 469px; }
  .action-related { left: 576px; }
  .video-title {
    position: absolute; left: 0; top: 506px; width: 839px; height: 53px;
    background: var(--title-band);
    font-family: "Arimo", sans-serif; font-weight: 400;
    font-size: 38.5px; line-height: 53px; padding-left: 36px;
    color: var(--text-soft); white-space: nowrap;
  }
  .video-details {
    position: absolute; left: 0; top: 559px; width: 839px; height: 149px;
    background: var(--body-bg);
  }
  .video-description {
    position: absolute; left: 36px; top: 3px;
    font-family: "Arimo", sans-serif; font-size: 20px; line-height: 27px;
    color: var(--text-light); white-space: nowrap;
  }
  .details-rule {
    position: absolute; left: 37px; top: 122px; width: 760px; height: 1px;
    background: var(--rule);
  }
  .app-footer {
    position: absolute; left: 0; top: 708px; width: 839px; height: 16px;
    background: var(--footer-bg);
  }
</style>
</head>
<body>
  <main class="app-screen">
    <header class="app-header">
      <h1 class="app-name">Kelvaro</h1>
      <svg class="header-search" width="36" height="36" viewBox="0 0 36 36" aria-label="Search">
        <circle cx="14" cy="14" r="10" fill="none" stroke="#fff" stroke-width="4.5"/>
        <line x1="21" y1="21" x2="31" y2="31" stroke="#fff" stroke-width="6" stroke-linecap="round"/>
      </svg>
      <svg class="header-menu" width="14" height="38" viewBox="0 0 14 38" aria-label="Menu">
        <rect x="0" y="0" width="14" height="4" fill="#fff"/>
        <rect x="0" y="16" width="14" height="4" fill="#fff"/>
        <rect x="0" y="32" width="14" height="4" fill="#fff"/>
      </svg>
    </header>

    <section class="video-player" aria-label="Video player">
      <svg class="play-button" width="52" height="48" viewBox="0 0 52 48" aria-label="Play">
        <polygon points="1,1 51,24 1,47" fill="#f2f2f2"/>
      </svg>
    </section>

    <nav class="video-actions">
      <div class="action action-watch">
        <svg width="34" height="34" viewBox="0 0 34 34"><rect x="13" y="0" width="8" height="34" fill="#fff"/><rect x="0" y="13" width="34" height="8" fill="#fff"/></svg>
        Watch Later
      </div>
      <div class="action action-like">
        <svg width="36" height="34" viewBox="0 0 36 34"><path d="M18 33 C6 23 0 17 0 9.5 C0 4 4 0 9.5 0 C13 0 16 2 18 5 C20 2 23 0 26.5 0 C32 0 36 4 36 9.5 C36 17 30 23 18 33 Z" fill="#fff"/></svg>
        Like
      </div>
      <div class="action action-share">
        <svg width="36" height="34" viewBox="0 0 36 34"><line x1="29" y1="6" x2="7" y2="17" stroke="#fff" stroke-width="3.5"/><line x1="7" y1="17" x2="29" y2="28" stroke="#fff" stroke-width="3.5"/><circle cx="29" cy="6" r="5.5" fill="#fff"/><circle cx="7" cy="17" r="5.5" fill="#fff"/><circle cx="29" cy="28" r="5.5" fill="#fff"/></svg>
        Share
      </div>
      <div class="action action-related">
        <svg width="34" height="34" viewBox="0 0 34 34"><rect x="0" y="0" width="15" height="15" fill="#fff"/><rect x="19" y="0" width="15" height="15" fill="#fff"/><rect x="0" y="19" width="15" height="15" fill="#fff"/><rect x="19" y="19" width="15" height="15" fill="#fff"/></svg>
        Related
      </div>
    </nav>

    <h2 class="video-title">Blandit elit commodo molestie</h2>

    <section class="video-details">
      <p class="video-description">Lorem ipsum dolor sit amet, consectetur adipiscing elit. Nulla quam velit,<br>vulputate eu pharetra nec, mattis ac neque. Duis vulputate commodo lectus, ac<br>blandit elit tincidunt id. Sed rhoncus, tortor sed eleifend tristique, tortor mauris</p>
      <div class="details-rule"></div>
    </section>

    <footer class="app-footer"></footer>
  </main>
</body>
</html>
```